Introducing A New Investment Management Boutique to Institutions, Professionals

4-page color brochure introducing a new investment management company to financial professionals and institutional investors. We want to quickly highlight some important distinctive features and stimulate curiosity to learn more about us and what we do. Relatively light on words (~700) this is about image - we are very good at what we do, and we add value by doing things a bit differently. So we do not want this to look like a typical financial services brochure. Please download the word doc for more guidance and the brochure text.

Target Market(s)

Investment industry professionals, consultants, foundations, endowments, wealthy individual investors

Industry/Entity Type

Investment Advisory

Font styles to use
Serif
Sans Serif

Colors
0355a3
3176b5
85acd3
cedeed

Requirements
Must have
• Convey an image of professionalism, expertise, confidence, independence from the crowd, trust.
Nice to have
• Some thematic design element supporting the story - whether of nature, or Wall Street and finance, or something else consistent with the words we provided. Microsoft Publisher (.pub) preferred, but .pdf (Adobe) format also acceptable.
Should not have
• Avoid using stock photos with people's faces. Should not have the feel of a mass market, consumer oriented product/service.

```html
<!DOCTYPE html>
<html lang="en">
<head>
<meta charset="utf-8">
<title>Harrowgate Capital – Brochure Spread</title>
<link rel="stylesheet" href="https://fonts.googleapis.com/css2?family=Cinzel:wght@500;600&family=Tinos:ital,wght@0,400;0,700;1,400&display=swap">
<style>
  :root{
    --blue-deep:#0355a3;
    --blue:#3176b5;
    --blue-soft:#85acd3;
    --blue-pale:#cedeed;
    --ink:#161616;
    --page-left:#dedfe1;
    --page-right:#f4f4f4;
    --backdrop:#e8e8e8;
  }
  *{box-sizing:border-box;margin:0;padding:0}
  html,body{width:1200px;height:900px;overflow:hidden;background:var(--backdrop)}
  body{font-family:'Tinos',serif;color:var(--ink)}
  .spread{position:absolute;left:120px;top:60px;width:960px;height:780px;display:flex;box-shadow:0 14px 40px rgba(0,0,0,.18)}
  .page{position:relative;width:480px;height:780px;padding:30px 34px 0;font-size:12px;line-height:1.27;display:flex;flex-direction:column}
  .page--left{background:var(--page-left);padding-bottom:48px}
  .page--right{background:var(--page-right);border-left:1px solid #cfcfcf;padding-bottom:18px}
  .page--left::after{content:"";position:absolute;left:0;right:0;bottom:0;height:34px;background:var(--blue-deep)}
  .page--right::after{content:"";position:absolute;left:0;right:0;bottom:0;height:8px;background:var(--blue-deep)}
  .section-title{font-family:'Cinzel',serif;font-weight:600;font-size:22px;letter-spacing:.5px;color:var(--ink);line-height:1.1;margin-bottom:5px}
  .section-title .accent{color:var(--blue)}
  .section-title--right{text-align:right}
  .section{margin-bottom:14px}
  .body-copy{margin-bottom:4px}
  .body-copy--center{text-align:center}
  .photo-area{width:200px;height:130px;margin:10px 0 0 140px;background:linear-gradient(135deg,#5d6f8c 0%,#2c3a55 55%,#10172a 100%)}
  .quote{font-style:italic;color:var(--blue);font-size:12px;margin-top:auto}
  .quote--left{padding-right:40px}
  .quote--right{padding-left:90px;text-align:right}
  .growth-row{display:flex;gap:14px;align-items:flex-start;margin-bottom:4px}
  .bullets{list-style:none;flex:1}
  .bullets li{position:relative;padding-left:14px;margin-bottom:2px}
  .bullets li::before{content:"";position:absolute;left:2px;top:5px;width:6px;height:6px;border-radius:50%;background:var(--blue)}
  .callout{width:165px;border:1px solid var(--ink);padding:6px 8px;font-style:italic;text-align:center;font-size:11.5px;background:#fff;margin-top:4px}
</style>
</head>
<body>
<main class="spread">
  <section class="page page--left">
    <div class="section">
      <h2 class="section-title">Different by <span class="accent">Design</span></h2>
      <p class="body-copy">Top investment performance seldom comes from following the crowd. It usually requires doing something unconventional. Harrowgate represents a compelling departure from our peers.</p>
      <p class="body-copy">Our distinctive philosophy, disciplined process, and solid historical performance place us among a select group of managers. We take pride in standing apart from our competition.</p>
    </div>
    <div class="section">
      <h2 class="section-title section-title--right">Singular <span class="accent">Perspective</span></h2>
      <p class="body-copy body-copy--center">Which path would you choose to guide your decisions: knowledge or speculation? In investing, facts beat forecasts, and we focus on what we can know.</p>
      <p class="body-copy body-copy--center">At Harrowgate, we look for companies whose growth is accelerating. Our original research is unbiased by consensus information, understanding the true drivers of growth and major risks.</p>
      <p class="body-copy body-copy--center">Our definition of growth and proprietary insight are key components of our competitive advantage.</p>
    </div>
    <div class="section">
      <h2 class="section-title">Concentrated <span class="accent">Portofolios</span></h2>
      <p class="body-copy">Equity managers typically own too many names, diluting their best ideas in overdiversified portfolios. Harrowgate portfolios are concentrated, exhibiting high conviction and high active share. Every position has the potential to contribute significantly. Research shows that more concentrated portfolios produce superior risk-adjusted returns.</p>
      <div class="photo-area" role="img" aria-label="Silhouette of a figure standing by a window with blinds, seen from behind in dark blue tones"></div>
    </div>
    <p class="quote quote--left">“No one can possibly achieve any real and lasting success by being a conformist.” – Walter Crane</p>
  </section>

  <section class="page page--right">
    <div class="section">
      <h2 class="section-title">Small Cap <span class="accent">Growth</span></h2>
      <p class="body-copy">With one chance to make a good first impression, small cap growth was the obvious choice for Harrowgate’s debut strategy.</p>
      <div class="growth-row">
        <ul class="bullets">
          <li>Our CIO has successfully managed small and mid cap portfolios for over 20 years</li>
          <li>Small cap offers the potential for significant alpha</li>
          <li>Modest asset base and relatively low turnover insulate us from liquidity constraints</li>
          <li>Many small cap managers are closed to new investors and we have capacity</li>
        </ul>
        <div class="callout">We know small cap.<br>Active management is rewarded.<br>We have a competitive edge.<br>We can meet a need.</div>
      </div>
      <p class="body-copy">The solid performance of this strategy since 2016 is consistent with the track record of similar portfolios managed by Martin Hale since 1999.</p>
    </div>
    <div class="section">
      <h2 class="section-title section-title--right">Uncorrelated <span class="accent">Alpha</span></h2>
      <p class="body-copy body-copy--center">At Harrowgate, we do not settle for performance that is slightly ahead of the benchmark. We aim to deliver exceptional risk-adjusted returns.</p>
      <p class="body-copy body-copy--center">Clients with multi-asset class portfolios look beyond a manager’s performance to consider the correlation between strategies and their diversifying impact on the overall portfolio. Managers, who typically are focused within their style box, rarely address this essential topic.</p>
      <p class="body-copy body-copy--center">Harrowgate appreciates the importance of low manager correlation to a client’s overall portfolio. Our process is designed to generate superior alpha at significantly lower correlation to a client’s other strategies.</p>
    </div>
    <div class="section">
      <h2 class="section-title">Defense <span class="accent">Wins Championship</span></h2>
      <p class="body-copy">The formula for investment success is pretty straightforward. Own more winners than losers. Since some losses are inevitable, our discipline is designed to minimize their impact.</p>
      <p class="body-copy">When the market environment turns unfriendly and risks outweigh opportunities, we focus aggressively on capital preservation. Long term investors should have an alternative to remaining fully invested through bear markets and absorbing significant paper losses. We work to limit the downside through strategic risk management – playing strong defense.</p>
      <p class="body-copy">A dollar not lost is a dollar gained, and over a market cycle minimizing losses can add real value.</p>
    </div>
    <p class="quote quote--right">“Any intelligent fool can make things bigger and more complex. It takes a touch of genius – and a lot of courage – to move in the opposite direction.” – Henry Ashford</p>
  </section>
</main>
</body>
</html>
```